HTML Web Design for RivoLink Website

I require a non functioning web design in HTML format.
The website is for an online platform for connecting contract geoscientists with employers looking for short term geologists and geophysicists.
There will be 12 pages plus 3 sub pages of design to complete in total, but for your submission, please provide three pages and one sub page for review. These are to be submitted upon you winning the design contest, and then you can complete the rest of the pages in the days following that.
Please provide your designs for the Home Page, Contractor Profile Page and the Search Page / Search Results List.
Please review my design brief, and mockup of some of the pages carefully. Also, please find attached my logo.
Note, my logo is red, but I do not want a red dominated design, please use red as an accent colour.

Target Market(s)

Geoscientists

Industry/Entity Type

Oil And Gas

Number of Pages Required

5+ page

Requirements
Must have
• HTML format designs
• Submit 3 pages for competition, but further pages after winner is selected
• Professional and modern
Nice to have
• Some red accent
Should not have
• Too much red

```html
<!DOCTYPE html>
<html lang="en">
<head>
<meta charset="utf-8">
<title>RivoLink – Contract Job Postings</title>
<link href="https://fonts.googleapis.com/css2?family=Raleway:wght@400;500;600;700&display=swap" rel="stylesheet">
<style>
:root{
  --red:#ee3f5a;
  --ink:#2a2a2a;
  --muted:#9a9a9a;
  --field:#f4f4f4;
  --field-line:#e3e3e3;
  --dark:#1d1f25;
  --contact-bg:#efefef;
  --links-bg:#f7f7f7;
  --copy-bg:#dedede;
  --white:#ffffff;
}
*{box-sizing:border-box;margin:0;padding:0}
html,body{width:782px;height:1200px;overflow:hidden;background:var(--white)}
body{font-family:"Raleway",sans-serif;color:var(--ink);position:relative}
.abs{position:absolute}
.hero-art{position:absolute;left:0;top:0}
.logo{left:14px;top:26px;font-size:27px;font-weight:700;color:var(--red);letter-spacing:-.5px}
.utility{left:456px;top:0;width:284px;height:29px}
.utility-links{left:470px;top:0;width:256px;height:29px;display:flex;justify-content:center;align-items:center;gap:7px;color:var(--white);font-size:9.5px}
.main-nav{left:338px;top:46px;display:flex;gap:15px;font-size:9.5px;font-weight:500}
.search{left:691px;top:41px;width:22px;height:22px;border:1.5px solid var(--red);border-radius:50%}
.page-title{left:120px;top:120px;color:var(--white);font-size:18.5px;font-weight:600}
.title-icon{left:91px;top:124px;width:14px;height:14px;background:var(--white)}
.tab{top:164px;height:26px;display:flex;align-items:center;justify-content:center;font-size:11px;color:var(--white)}
.tab-active{left:112px;width:140px;background:var(--red);clip-path:polygon(12px 0,130px 0,140px 100%,0 100%)}
.tab-alt{left:252px;width:262px;background:var(--dark);font-size:10px;clip-path:polygon(10px 0,250px 0,262px 100%,0 100%)}
.form-card{left:88px;top:190px;width:603px;height:625px;border:2px solid var(--red);background:var(--white)}
.label{left:116px;font-size:9.3px;line-height:13.5px;color:var(--ink)}
.field{background:var(--field);border:1px solid var(--field-line);font-size:8px;color:var(--muted);padding:0 9px;display:flex;align-items:center;justify-content:space-between}
.field.tall{align-items:flex-start;padding-top:7px}
.chev{width:6px;height:6px;border-right:1.3px solid var(--red);border-bottom:1.3px solid var(--red);transform:rotate(45deg);margin-top:-3px}
.choice{font-size:9px;color:#666;display:flex;align-items:center;gap:6px}
.box{width:7px;height:7px;border:1px solid #bbb;display:inline-block}
.box.on{border-color:var(--red);background:radial-gradient(var(--red) 55%,transparent 56%);background:var(--red);box-shadow:inset 0 0 0 1.5px #fff}
.note{left:331px;top:316px;width:330px;font-size:6.8px;line-height:13px;color:#666}
.notice{left:114px;top:583px;width:553px;height:55px;background:var(--field);border:1px solid var(--field-line)}
.notice-text{left:126px;top:592px;width:380px;font-size:9px;line-height:13.5px;color:#777}
.btn-solid{background:var(--red);color:var(--white);font-weight:700;font-size:9.5px;display:flex;align-items:center;justify-content:center}
.btn-line{border:1px solid #999;background:var(--white);color:var(--ink);font-weight:700;font-size:10px;display:flex;align-items:center;justify-content:center}
.rss{left:0;top:832px;width:782px;height:134px;background:var(--dark);color:var(--white)}
.rss-title{left:116px;top:849px;font-size:18px;font-weight:700;color:var(--white)}
.rss-col{top:882px;width:200px;color:var(--white)}
.rss-col h3{font-size:10px;font-weight:700;margin-bottom:7px}
.rss-col p{font-size:7px;line-height:13px}
.contact{left:0;top:966px;width:782px;height:187px;background:var(--contact-bg)}
.h2{font-size:18px;font-weight:600;color:var(--ink)}
.input{border-bottom:1px solid var(--red);font-size:10px;padding-left:2px;height:20px}
.loc-line{left:568px;font-size:8px;line-height:13.5px;color:#333}
.social{top:1110px;width:20px;height:20px;border-radius:50%;background:#aaa}
.footer-links{left:0;top:1153px;width:782px;height:22px;background:var(--links-bg);display:flex;justify-content:center;align-items:center;gap:18px;font-size:8.3px;font-weight:500}
.copyright{left:0;top:1175px;width:782px;height:25px;background:var(--copy-bg);display:flex;justify-content:center;align-items:center;font-size:7px}
</style>
</head>
<body>

<svg class="hero-art" width="782" height="420" viewBox="0 0 782 420" role="img" aria-label="Dusk photo of an offshore drilling vessel on calm water">
  <defs>
    <linearGradient id="dusk" x1="0" y1="0" x2="1" y2="1">
      <stop offset="0" stop-color="#3e5868"/>
      <stop offset=".55" stop-color="#5f7380"/>
      <stop offset="1" stop-color="#8e8a86"/>
    </linearGradient>
  </defs>
  <polygon points="0,180 134,74 444,74 320,190 88,190 88,414 0,414" fill="url(#dusk)"/>
  <line x1="228" y1="0" x2="0" y2="180" stroke="#ee3f5a" stroke-width="2"/>
</svg>

<div class="abs logo">RivoLink</div>

<svg class="abs utility" viewBox="0 0 284 29"><polygon points="0,0 284,0 266,29 18,29" fill="#ee3f5a"/></svg>
<nav class="abs utility-links"><span>Job Postings</span><span>|</span><span>Resources</span><span>|</span><span>Articles</span><span>|</span><span>Contact</span></nav>

<nav class="abs main-nav"><span>Home</span><span>How it Works</span><span>Contractor Profile</span><span>Employer Favourites</span><span>Analytics</span></nav>
<svg class="abs" style="left:691px;top:41px" width="22" height="22" viewBox="0 0 22 22"><circle cx="11" cy="11" r="10" fill="none" stroke="#ee3f5a" stroke-width="1.5"/><circle cx="10" cy="10" r="3.5" fill="none" stroke="#ee3f5a" stroke-width="1.6"/><line x1="12.6" y1="12.6" x2="15" y2="15" stroke="#ee3f5a" stroke-width="1.8"/></svg>

<svg class="abs" style="left:91px;top:123px" width="15" height="15" viewBox="0 0 15 15"><rect x="0" y="0" width="15" height="15" fill="#fff"/><polygon points="6,2 9,2 8.5,5 10,11 7.5,13 5,11 6.5,5" fill="#3e5868"/></svg>
<h1 class="abs page-title">Contract Job postings</h1>

<div class="abs tab tab-active">The job postings</div>
<div class="abs tab tab-alt">Work for Equity/Deferred Payment Postings</div>

<section class="abs form-card"></section>

<div class="abs label" style="top:207px">The country the work is required in</div>
<div class="abs field" style="left:331px;top:203px;width:164px;height:23px"><span></span><i class="chev"></i></div>

<div class="abs label" style="top:241px">Whether or not travel is required</div>
<div class="abs choice" style="left:333px;top:242px"><span class="box on"></span>Yes</div>
<div class="abs choice" style="left:384px;top:242px"><span class="box"></span>No</div>

<div class="abs label" style="top:269px">If the contractors can</div>
<div class="abs choice" style="left:333px;top:271px"><span class="box on"></span>Work remotely</div>
<div class="abs choice" style="left:434px;top:271px"><span class="box"></span>In-house</div>

<div class="abs label" style="top:298px">Choose the advertisement period</div>
<div class="abs choice" style="left:333px;top:300px"><span class="box on"></span>7 days</div>
<div class="abs choice" style="left:389px;top:300px"><span class="box"></span>14 days</div>
<div class="abs choice" style="left:446px;top:300px"><span class="box"></span>21days</div>
<div class="abs note">(When the posting has expired it remains on the site greyed out with the word EXPIRED stamped across it for a further 3 months.)</div>

<div class="abs label" style="top:354px">The expected duration of the job</div>
<div class="abs field" style="left:331px;top:349px;width:164px;height:23px"><span>Enter the Duration</span><i class="chev"></i></div>

<div class="abs label" style="top:384px">The expected start date</div>
<div class="abs field" style="left:331px;top:379px;width:164px;height:23px"><span>DD / MM /&nbsp; YYYY</span></div>

<div class="abs label" style="top:415px;width:190px">The type of project from a list which the employer can add to in other which then becomes part of the list</div>
<div class="abs field" style="left:331px;top:411px;width:164px;height:23px"><span>New business asset review</span><i class="chev"></i></div>

<div class="abs label" style="top:467px">A short description of the project</div>
<div class="abs field tall" style="left:331px;top:462px;width:336px;height:41px"><span>A short description of the project</span></div>

<div class="abs label" style="top:517px">What type of contractor(s)</div>
<div class="abs field" style="left:331px;top:512px;width:107px;height:23px"><span>Mining</span><i class="chev"></i></div>
<div class="abs label" style="left:455px;top:517px">Number of Contractors</div>
<div class="abs field" style="left:561px;top:512px;width:106px;height:23px"><span>10 nos</span><i class="chev"></i></div>

<div class="abs label" style="top:550px">Exact day rate Offer</div>
<div class="abs field" style="left:331px;top:545px;width:107px;height:23px"><span>$$</span></div>
<div class="abs label" style="left:455px;top:550px">Or&nbsp; Maximum Day rate</div>
<div class="abs field" style="left:561px;top:545px;width:106px;height:23px"><span>$$</span></div>

<div class="abs notice"></div>
<p class="abs notice-text">Enter your Job Postings appear as a job card on the Contract Job Postings page, with the newest posts at the top</p>
<div class="abs btn-solid" style="left:553px;top:598px;width:93px;height:21px">Submit</div>

<div class="abs label" style="top:656px;width:200px">The contractors can register their interest via a blind bidding where they may offer their services at full price or at a discount.</div>
<div class="abs field" style="left:331px;top:652px;width:164px;height:23px"><span>$$&nbsp;&nbsp; blind bidding</span></div>

<div class="abs label" style="top:706px">Contractor relevant experience</div>
<div class="abs field tall" style="left:331px;top:703px;width:336px;height:39px"><span>Up to 200 words</span></div>

<div class="abs btn-solid" style="left:282px;top:763px;width:66px;height:18px;font-size:10px">Delete</div>
<div class="abs btn-line" style="left:355px;top:763px;width:71px;height:18px">Suspend</div>
<div class="abs btn-line" style="left:434px;top:763px;width:65px;height:18px">Re - list</div>

<section class="abs rss"></section>
<svg class="abs" style="left:83px;top:852px" width="16" height="16" viewBox="0 0 16 16"><circle cx="3" cy="13" r="2" fill="#fff"/><path d="M1 7a8 8 0 0 1 8 8" fill="none" stroke="#fff" stroke-width="2"/><path d="M1 2a13 13 0 0 1 13 13" fill="none" stroke="#fff" stroke-width="2"/></svg>
<h2 class="abs rss-title">RSS Feed</h2>
<article class="abs rss-col" style="left:78px"><h3>Neque porro quisquam est qui dolorem</h3><p>Lorem Ipsum is simply dummy text of the printing and typesetting industry.</p></article>
<article class="abs rss-col" style="left:296px"><h3>Neque porro quisquam est qui dolorem</h3><p>Lorem Ipsum is simply dummy text of the printing and typesetting industry.</p></article>
<article class="abs rss-col" style="left:510px"><h3>Neque porro quisquam est qui dolorem</h3><p>Lorem Ipsum is simply dummy text of the printing and typesetting industry.</p></article>

<section class="abs contact"></section>
<h2 class="abs h2" style="left:78px;top:982px">Contact Us</h2>
<div class="abs input" style="left:80px;top:1016px;width:197px">Name</div>
<div class="abs input" style="left:293px;top:1016px;width:197px">Email</div>
<div class="abs input" style="left:80px;top:1062px;width:410px;padding-left:3px">Message</div>
<div class="abs" style="left:80px;top:1106px;width:73px;height:24px;border:1.5px solid var(--red);color:var(--red);font-weight:700;font-size:10px;display:flex;align-items:center;justify-content:center">Submit</div>

<h2 class="abs h2" style="left:551px;top:982px">Location</h2>
<svg class="abs" style="left:552px;top:1027px" width="8" height="11" viewBox="0 0 8 11"><path d="M4 0a4 4 0 0 1 4 4c0 3-4 7-4 7S0 7 0 4a4 4 0 0 1 4-4z" fill="#222"/><circle cx="4" cy="4" r="1.5" fill="#efefef"/></svg>
<div class="abs loc-line" style="top:1023px">Unit 4, 220 Larchmont<br>Road Eastfield</div>
<svg class="abs" style="left:552px;top:1064px" width="9" height="9" viewBox="0 0 9 9"><path d="M1 0h2l1 2.3-1.2 1a5 5 0 0 0 2.9 2.9l1-1.2L9 6v2a1 1 0 0 1-1 1A8 8 0 0 1 0 1a1 1 0 0 1 1-1z" fill="#222"/></svg>
<div class="abs loc-line" style="top:1063px">(555)-018-2247</div>
<svg class="abs" style="left:552px;top:1085px" width="9" height="7" viewBox="0 0 9 7"><rect width="9" height="7" fill="#222"/><path d="M0 0l4.5 3.5L9 0" fill="none" stroke="#efefef" stroke-width="1"/></svg>
<div class="abs loc-line" style="top:1082px">hello@rivolink-example.com</div>
<span class="abs social" style="left:551px"></span>
<span class="abs social" style="left:573px"></span>
<span class="abs social" style="left:596px"></span>
<span class="abs social" style="left:618px"></span>

<nav class="abs footer-links"><span>Home</span><span>Contractor Profile</span><span>Employer Search</span><span>Contract job Posting</span><span>Articles</span><span>Resources</span><span>Payment Checkout</span><span>Contact Us</span></nav>
<footer class="abs copyright">Copyrights © 2017, www.rivolink-example.com. All Rights Reserved.</footer>

</body>
</html>
```